Flyer for an online formula one racing league

Hello.

I am looking for the perfect one page facebook/instagram style flyer for an online formula one racing league. The racing league is called 'VOLKA RACING LEAGUE'.

Information that MUST be on the new flyer is already on the old flyer I have uploaded here. In addition to including: The Volka racing league 'R' logo I have uploaded AND the text: 'Very popular, clean and competitive racing league, running for its 4th season. Why not join with a friend? Race times, Mondays, Tuesdays and Wednesdays each at 8pm UK TIME Message below for any questions. (Spacing of information is not important, however all the information in regards to the racing I have just mentioned MUST BE on the flyer, this includes info from old pic, logo and the other info I just mentioned).

It would be beneficial to have lots of dark blue on the flyer and the new flyer to be a lot different to the original flyer I uploaded, but this is not essential.

I apologise if I did not explain very well, any questions, please message me.

The best flyer should look the most attractive to someone that might be interested in joining an online formula one racing league.

I used this website before to create the perfect logo for my Sunday League team last year, and I was very impressed. I look forward to seeing your submissions.

Target Market(s)

No specific target, more something that may attract someone into joining a formula one online racing league

Industry/Entity Type

e sports/formula one

Colors
0054AA
0677BA
7BADD7
CADEEF
E8F1F8

Requirements
Must have
• Read product description please
Should not have
• Ignoring product description!

```html
<!DOCTYPE html>
<html lang="en">
<head>
<meta charset="utf-8">
<title>Volka Racing League – Flyer</title>
<link href="https://fonts.googleapis.com/css2?family=Bebas+Neue&display=swap" rel="stylesheet">
<style>
  :root {
    --navy-deep: #060a5e;
    --navy: #0b1496;
    --royal: #1a2ccf;
    --electric: #2a3ff0;
    --badge: #0d1033;
    --white: #ffffff;
    --lavender: #8c90ec;
    --magenta: #e3157f;
  }
  * { margin: 0; padding: 0; box-sizing: border-box; }
  html, body {
    width: 1200px;
    height: 628px;
    overflow: hidden;
    background: var(--navy-deep);
  }
  .flyer {
    position: relative;
    width: 1200px;
    height: 628px;
    overflow: hidden;
    font-family: "Bebas Neue", "Oswald", sans-serif;
    color: var(--white);
  }
  .hero-backdrop {
    position: absolute;
    inset: 0;
    background:
      radial-gradient(ellipse 40% 35% at 58% 62%, rgba(20, 30, 140, 0.9), transparent 70%),
      linear-gradient(170deg, var(--navy-deep) 0%, var(--navy) 30%, var(--royal) 55%, var(--navy) 78%, var(--navy-deep) 100%);
  }
  .brand-badge {
    position: absolute;
    top: 38px;
    width: 132px;
    height: 132px;
    border-radius: 50%;
    background: var(--badge);
    display: flex;
    align-items: center;
    justify-content: center;
    font-size: 40px;
    letter-spacing: 1px;
    color: var(--white);
  }
  .brand-badge--left { left: 38px; }
  .brand-badge--right { right: 38px; }
  .league-title {
    position: absolute;
    top: 30px;
    left: 0;
    width: 100%;
    text-align: center;
    font-size: 104px;
    font-weight: 400;
    line-height: 1;
    letter-spacing: 1px;
  }
  .league-tagline {
    position: absolute;
    top: 150px;
    left: 0;
    width: 100%;
    text-align: center;
    color: var(--lavender);
    font-size: 41px;
    line-height: 50px;
    letter-spacing: 0.5px;
  }
  .race-schedule {
    position: absolute;
    top: 283px;
    left: 52px;
    font-size: 48px;
    line-height: 50px;
    letter-spacing: 0.5px;
  }
  .race-schedule .schedule-heading { margin-bottom: 0; }
  .call-to-action {
    position: absolute;
    right: 40px;
    top: 508px;
    text-align: right;
  }
  .call-to-action .invite {
    color: var(--magenta);
    font-size: 41px;
    line-height: 46px;
    letter-spacing: 0.5px;
  }
  .call-to-action .contact-note {
    font-size: 25px;
    line-height: 34px;
    letter-spacing: 3.2px;
    margin-top: 4px;
  }
</style>
</head>
<body>
  <main class="flyer">
    <div class="hero-backdrop" role="img" aria-label="Motion-blurred photograph of a single-seater racing car speeding across the frame, tinted deep blue"></div>

    <div class="brand-badge brand-badge--left">Volka</div>
    <div class="brand-badge brand-badge--right">Volka</div>

    <h1 class="league-title">VOLKA RACING LEAGUE</h1>

    <p class="league-tagline">
      Very popular, clean and competitive racing league<br>
      Running for its 4th season!
    </p>

    <section class="race-schedule">
      <p class="schedule-heading">Racing times:</p>
      <p>Mondays, Tuesdays and Wednesdays</p>
      <p>Each at 8pm UK time</p>
    </section>

    <section class="call-to-action">
      <p class="invite">Why not join with a friend?</p>
      <p class="contact-note">Message below for any questions</p>
    </section>
  </main>
</body>
</html>
```